Agricultural Consulting Website

Provide a modern yet business like website for my new Agriculture Consulting Business in Australia called FenTrove. Whilst we are based in Australia we are targetting both domestic and international markets (especially in Asia). We are targetting corporate, small business, government and farmer clients. The design should compliment our logo also sourced through pixel guild. The webiste should be easy for me to keep updated on a regular basis without the need to go back to the designer.

Industry/Entity Type

Business

Requirements
Must have
• clean crisp feel
• be modern yet business like
• be able to be updated by myself easily

```html
<!DOCTYPE html>
<html lang="en">
<head>
<meta charset="utf-8">
<title>FenTrove – Agricultural Consulting</title>
<link href="https://fonts.googleapis.com/css2?family=Mystery+Quest&family=Roboto+Condensed:wght@400;700&family=Arimo:wght@400;700&family=Sniglet&display=swap" rel="stylesheet">
<style>
:root{
  --ink:#141414;
  --brown:#5b3412;
  --brown-dark:#4a290c;
  --green:#5f9e16;
  --green-light:#7cb82a;
  --orange:#e39a1c;
  --blue:#1d6c9a;
  --paper:#ececec;
  --white:#ffffff;
  --text:#1e1e1e;
  --grey-line:#c9c9c9;
}
*{box-sizing:border-box;margin:0;padding:0}
html,body{width:812px;height:1200px;overflow:hidden}
body{position:relative;background:var(--paper);font-family:"Arimo",Arial,sans-serif;color:var(--text)}
.abs{position:absolute}

/* top bar */
.topbar{left:0;top:0;width:812px;height:43px;background:var(--ink)}
.call{right:118px;top:17px;font:700 11px "Roboto Condensed",sans-serif;color:var(--green-light);letter-spacing:.3px}
.call span{color:var(--orange)}
.stripe{top:43px;height:5px}

/* header */
.header{left:0;top:48px;width:812px;height:358px;background:linear-gradient(135deg,#603713,#4e2b0d)}
.logo-tab{left:116px;top:48px;width:172px;height:84px}
.brand{display:flex;align-items:center;gap:8px;font-family:"Sniglet",sans-serif;color:var(--green);font-size:27px}
.brand i{display:block;width:26px;height:26px;background:var(--brown)}
.logo-tab .brand{position:absolute;left:14px;top:18px}
.search{left:568px;top:74px;width:124px;height:18px;background:var(--white);font:11px "Arimo",sans-serif;color:#333;padding:3px 0 0 19px}
.search svg{position:absolute;right:5px;top:3px}
.nav{left:400px;top:109px;display:flex}
.nav a{font:700 11px "Roboto Condensed",sans-serif;color:var(--white);text-decoration:none;height:21px;line-height:21px;padding:0 8px;margin-right:10px}
.nav a.active{background:var(--green);padding:0 9px}

/* slider */
.slider{left:118px;top:144px;width:574px;height:242px;background:#e9e9e9;border-radius:6px;box-shadow:0 3px 6px rgba(0,0,0,.35)}
.slide{left:127px;top:154px;width:557px;height:220px;border-radius:3px;background:linear-gradient(180deg,#b7c3cc 0%,#a6b7a8 14%,#5d9a3a 26%,#3f8a24 55%,#2f7419 100%)}
.arrow{width:50px;height:50px;border-radius:50%;background:#e9e9e9;top:231px}
.arrow b{position:absolute;left:11px;top:11px;width:28px;height:28px;border-radius:50%;background:#8a8a8a}
.arrow svg{position:absolute;left:11px;top:11px}

/* features */
.feature-photo{width:160px;height:160px;border-radius:50%;background:var(--white);box-shadow:0 2px 5px rgba(0,0,0,.25)}
.feature-photo span{position:absolute;left:6px;top:6px;width:148px;height:148px;border-radius:50%}
.feature-title{width:220px;text-align:center;top:603px;font:17px "Mystery Quest",cursive;color:var(--brown);white-space:nowrap}
.card{top:638px;width:146px;height:188px;background:var(--white);border-top:5px solid var(--brown);box-shadow:1px 2px 4px rgba(0,0,0,.3)}
.card .badge{position:absolute;left:50%;top:-14px;transform:translateX(-50%);width:36px;height:36px;border-radius:50%;background:var(--white)}
.card .badge i{position:absolute;left:9px;top:10px;width:18px;height:18px;border-radius:50%;background:var(--brown)}
.card p{position:absolute;left:6px;right:6px;top:40px;font-size:8.6px;line-height:12.4px;text-align:center}

/* divider */
.divider{left:0;top:866px;width:812px;height:1px;background:var(--grey-line)}
.divider-brand{left:336px;top:849px;background:var(--paper);padding:0 10px}
.divider-brand .brand{font-size:26px}

/* lower columns */
.col-title{top:911px;font:17px "Mystery Quest",cursive;color:var(--brown);white-space:nowrap}
.col-title em{font-style:normal;color:var(--green)}
.welcome p{font-size:8.6px;line-height:15.6px}
.btn{height:15px;padding:0 8px;background:var(--brown);color:var(--white);font:700 8.5px "Arimo",sans-serif;line-height:15px;border-radius:2px}
.vsep{top:905px;width:0;height:195px;border-left:1px dotted #9a9a9a}
.news-item .date{font:700 8.5px "Arimo",sans-serif;color:var(--brown)}
.news-item .quote{font-size:7.6px;line-height:10px;margin-top:5px}
.news-item .by{font-size:9px;color:var(--green);margin-top:6px}
.news-rule{left:326px;top:1002px;width:178px;border-top:1px dotted #555}
.login label{display:block;font:8.5px "Arimo",sans-serif;margin-bottom:4px}
.field{width:146px;height:19px;background:var(--white)}
.remember{font-size:8.5px;display:flex;align-items:center;gap:7px}
.remember i{display:block;width:10px;height:10px;border-radius:50%;background:var(--white)}

/* footer */
.footer{left:0;top:1110px;width:812px;height:90px;background:var(--ink)}
.follow{left:152px;top:1132px;font:700 10px "Arimo",sans-serif;color:var(--white)}
.social{left:142px;top:1154px;display:flex;gap:10px}
.social i{display:block;width:18px;height:18px;border-radius:50%;background:#d9d9d9}
.footer-links{left:316px;top:1134px;font-size:9px;display:flex;gap:7px;color:var(--white)}
.copyright{left:376px;top:1153px;font-size:8.5px;color:var(--white)}
.footer-brand{left:577px;top:1134px}
.footer-brand .brand{color:var(--white);font-size:25px}
.footer-brand .brand i{background:var(--white)}
</style>
</head>
<body>

<div class="abs topbar"></div>
<div class="abs call">CALL US: <span>222-555-014</span></div>
<div class="abs stripe" style="left:0;width:198px;background:var(--blue)"></div>
<div class="abs stripe" style="left:198px;width:90px;background:var(--brown-dark)"></div>
<div class="abs stripe" style="left:288px;width:118px;background:var(--green)"></div>
<div class="abs stripe" style="left:406px;width:208px;background:var(--brown-dark)"></div>
<div class="abs stripe" style="left:614px;width:198px;background:var(--orange)"></div>

<header>
  <div class="abs header"></div>
  <svg class="abs logo-tab" width="172" height="84" viewBox="0 0 172 84" aria-hidden="true">
    <polygon points="0,0 172,0 172,74 86,82 0,74" fill="#fff"/>
  </svg>
  <div class="abs logo-tab"><div class="brand"><i></i>FenTrove</div></div>

  <div class="abs search">Search
    <svg width="12" height="12" viewBox="0 0 12 12" aria-hidden="true"><circle cx="5" cy="5" r="3.6" fill="none" stroke="#333" stroke-width="1.5"/><line x1="7.6" y1="7.6" x2="11" y2="11" stroke="#333" stroke-width="2"/></svg>
  </div>

  <nav class="abs nav">
    <a class="active" href="#">HOME</a><a href="#">ABOUT US</a><a href="#">PRODUCTS</a><a href="#">SERVICES</a><a href="#">CONTACTS</a>
  </nav>

  <div class="abs slider"></div>
  <div class="abs slide" role="img" aria-label="Photo of irrigated green crop rows stretching to distant hills"></div>
  <div class="abs arrow" style="left:93px"><b></b>
    <svg width="28" height="28" viewBox="0 0 28 28" aria-hidden="true"><path d="M17 8 L10 14 L17 20" fill="none" stroke="#fff" stroke-width="3"/></svg></div>
  <div class="abs arrow" style="left:667px"><b></b>
    <svg width="28" height="28" viewBox="0 0 28 28" aria-hidden="true"><path d="M11 8 L18 14 L11 20" fill="none" stroke="#fff" stroke-width="3"/></svg></div>
</header>

<main>
  <div class="abs feature-photo" style="left:115px;top:430px"><span style="background:radial-gradient(circle,#8a6a4a,#3d2c1c)" role="img" aria-label="Photo of hands planting a seedling in soil"></span></div>
  <div class="abs feature-photo" style="left:327px;top:430px"><span style="background:radial-gradient(circle,#5f8a3a,#2e4a22)" role="img" aria-label="Photo of a worker harvesting leafy greens"></span></div>
  <div class="abs feature-photo" style="left:540px;top:430px"><span style="background:radial-gradient(circle,#c2512e,#4a5a2a)" role="img" aria-label="Photo of a pile of fresh vegetables"></span></div>

  <h2 class="abs feature-title" style="left:84px">CAREFUL CULTIVATION</h2>
  <h2 class="abs feature-title" style="left:297px">TIMELY HARVESTING</h2>
  <h2 class="abs feature-title" style="left:510px">PREMIUM PRODUCTS</h2>

  <div class="abs card" style="left:118px"><div class="badge"><i></i></div>
    <p>Lorem Ipsum is simply dummy text of the printing and typesetting industry. Lorem Ipsum has been the industry's standard dummy text ever since the 1500s, when an unknown printer took a galley of type and scrambled it to make a type specimen book. It has survived not only five centuries, but also the leap</p></div>
  <div class="abs card" style="left:334px"><div class="badge"><i></i></div>
    <p>Lorem Ipsum is simply dummy text of the printing and typesetting industry. Lorem Ipsum has been the industry's standard dummy text ever since the 1500s, when an unknown printer took a galley of type and scrambled it to make a type specimen book. It has survived not only five centuries, but also the leap</p></div>
  <div class="abs card" style="left:548px"><div class="badge"><i></i></div>
    <p>Lorem Ipsum is simply dummy text of the printing and typesetting industry. Lorem Ipsum has been the industry's standard dummy text ever since the 1500s, when an unknown printer took a galley of type and scrambled it to make a type specimen book. It has survived not only five centuries, but also the leap</p></div>

  <div class="abs divider"></div>
  <div class="abs divider-brand"><div class="brand"><i></i>FenTrove</div></div>

  <section class="welcome">
    <h3 class="abs col-title" style="left:110px">WELCOME TO <em>OUR SITE.</em></h3>
    <p class="abs" style="left:110px;top:939px;width:192px">Lorem Ipsum is simply dummy text of the printing and typesetting industry. Lorem Ipsum has been the industry's standard dummy text ever since the 1500s, when an unknown printer took a galley of type and scrambled it to make a type specimen book. It has survived not only five centuries, but also the leap into electronic typesetting, remaining essentially unchanged.</p>
    <div class="abs btn" style="left:234px;top:1073px">+ READ MORE</div>
  </section>

  <div class="abs vsep" style="left:312px"></div>
  <div class="abs vsep" style="left:518px"></div>

  <section class="news">
    <h3 class="abs col-title" style="left:363px">LETEST <em>NEWS</em></h3>
    <div class="abs news-item" style="left:326px;top:939px;width:178px">
      <div class="date">( NOVEMBER 11,&nbsp; 2013 )</div>
      <div class="quote">“ Lorem Ipsum is simply dummy text of the printing and typesetting industry.”</div>
      <div class="by">Dara Ellison, Brookvale Co.</div>
    </div>
    <div class="abs news-rule"></div>
    <div class="abs news-item" style="left:326px;top:1013px;width:178px">
      <div class="date">( NOVEMBER 11,&nbsp; 2013 )</div>
      <div class="quote">“ Lorem Ipsum is simply dummy text of the printing and typesetting industry.”</div>
      <div class="by">Dara Ellison, Brookvale Co.</div>
    </div>
    <div class="abs btn" style="left:442px;top:1073px">+ READ MORE</div>
  </section>

  <section class="login">
    <h3 class="abs col-title" style="left:592px">LOGIN</h3>
    <div class="abs" style="left:549px;top:946px"><label>USERNAME:</label><div class="field"></div></div>
    <div class="abs" style="left:549px;top:992px"><label>PASSWORD:</label><div class="field"></div></div>
    <div class="abs remember" style="left:549px;top:1043px"><i></i>Remember me</div>
    <div class="abs btn" style="left:549px;top:1073px">LOGIN &gt;&gt;</div>
  </section>
</main>

<footer>
  <div class="abs footer"></div>
  <div class="abs follow">FOLLOW US:</div>
  <div class="abs social" aria-label="Social links"><i></i><i></i><i></i></div>
  <div class="abs footer-links"><span>HOME</span><span>ABOUT US</span><span>PRODUCT</span><span>SERVICES</span><span>CONTACT US</span></div>
  <div class="abs copyright">COPY-RIGHT@FENTROVE</div>
  <div class="abs footer-brand"><div class="brand"><i></i>FenTrove</div></div>
</footer>

</body>
</html>
```